emerald card

Bellavore/Gems
Est.1972
We are a direct Importer of Colombian Emeralds, with gem lab certificates KSL,PRV 1.0ct. and over.Gem ID and Country of origin
Dale Montrose belmo@postwire.example
469 552 0187 www. bellavoregold.example
The current web page is being redesigned,please ,Bellavore/Gems is a new company. We specialize in Colombian Emeralds.
Some of the designers used the existing web page and companies and created business cards for the wrong companies.
The blue back ground deign from Sri Lanka is the only card design that has all the correct information.

Target Market(s)

Fine Jewelry

Industry/Entity Type

Business

Contact Information for Business Card

Bellavore/Gems

Font styles to use
Other font styles liked:
• Roman

Requirements
Must have
• Bellavore/Gems Dale Montrose
P.O.Box 318827 Dallas,Tx.75219 Ph. 469 552 0187 E-Mail:belmo@postwire.example
www.bellavoregold.example, Emeralds over 1.0ct. are certified for Country of origin and Gem ID-KSL or PRV cerificates.

We are importers of Colombian Emeralds all Emeralds over 1.0ct.
Dallas,Tx. 75219
KSL,PRV
Nice to have
• Picture of Emerald
Should not have
• No other company names
We are changing information on our web site.do not use the web page for design.

```html
<!DOCTYPE html>
<html lang="en">
<head>
<meta charset="utf-8">
<title>Bellavore/Gems – Dale Montrose Business Card</title>
<link rel="stylesheet" href="https://fonts.googleapis.com/css2?family=Open+Sans:wght@400;600&family=Crimson+Pro:wght@400&display=swap">
<style>
  :root {
    --backdrop: #e4e4e4;
    --paper: #ffffff;
    --ink: #111111;
    --ruby: #9e1f23;
    --ruby-deep: #7a2221;
    --night: #221c1f;
    --gold: #e6a52e;
    --emerald-light: #3fbf6e;
    --emerald: #138a3e;
    --emerald-dark: #063a1c;
  }
  * { box-sizing: border-box; margin: 0; padding: 0; }
  html, body {
    width: 992px; height: 1200px; overflow: hidden;
    background: var(--backdrop);
  }
  .canvas { position: relative; width: 992px; height: 1200px; }
  .card {
    position: absolute; left: 62px; width: 868px; height: 495px;
    overflow: hidden;
  }
  .card--front { top: 62px; background: var(--paper); }
  .card--back {
    top: 637px;
    background: linear-gradient(180deg, var(--ruby) 0%, var(--ruby-deep) 35%, var(--night) 100%);
  }

  /* front */
  .front__band {
    position: absolute; left: 0; right: 0; top: 280px; bottom: 0;
    background: linear-gradient(180deg, var(--ruby) 0%, var(--ruby-deep) 40%, var(--night) 100%);
  }
  .front__rule {
    position: absolute; left: 0; right: 0; top: 268px; height: 6px;
    background: var(--ruby);
  }
  .front__emerald { position: absolute; left: 470px; top: 0; width: 398px; height: 380px; }
  .front__name {
    position: absolute; left: 44px; top: 40px;
    font: 400 40px/1 "Open Sans", sans-serif; color: var(--ink);
  }
  .front__phone, .front__address {
    position: absolute; left: 45px;
    font: 400 16px/1 "Open Sans", sans-serif; color: var(--ink);
  }
  .front__phone { top: 94px; }
  .front__address { top: 116px; }
  .front__field {
    position: absolute; left: 45px;
    font: 600 22px/1 "Open Sans", sans-serif; color: var(--ink);
    font-variant: small-caps; letter-spacing: 0.4px;
  }
  .front__field--gem { top: 162px; }
  .front__field--origin { top: 214px; }
  .contacts { position: absolute; left: 44px; top: 338px; list-style: none; }
  .contacts li {
    display: flex; align-items: center; height: 40px;
    font: 400 22px/1 "Open Sans", sans-serif; color: var(--gold); letter-spacing: 0.3px;
  }
  .contacts svg { width: 22px; height: 22px; margin-right: 28px; flex: none; }

  /* back */
  .back__emerald { position: absolute; left: 382px; top: 132px; width: 97px; height: 97px; }
  .back__company {
    position: absolute; left: 0; right: 0; top: 236px; text-align: center;
    font: 400 46px/1 "Crimson Pro", serif; color: var(--gold);
  }
  .back__est {
    position: absolute; left: 0; right: 0; top: 292px; text-align: center;
    font: 400 21px/1 "Crimson Pro", serif; color: var(--gold);
  }
  .back__certs {
    position: absolute; left: 0; right: 0; top: 338px; text-align: center;
    font: 400 19px/1.3 "Crimson Pro", serif; color: var(--gold);
  }
  .back__web {
    position: absolute; left: 0; right: 0; top: 424px; text-align: center;
    font: 400 27px/1 "Crimson Pro", serif; color: var(--gold); letter-spacing: 0.3px;
  }
</style>
</head>
<body>
<main class="canvas">

  <section class="card card--front">
    <div class="front__band"></div>
    <div class="front__rule"></div>
    <svg class="front__emerald" viewBox="0 0 398 380" role="img" aria-label="Photograph of a cut emerald gemstone">
      <defs>
        <linearGradient id="emerald-large" x1="0" y1="0" x2="1" y2="1">
          <stop offset="0" stop-color="var(--emerald-light)"/>
          <stop offset="0.5" stop-color="var(--emerald)"/>
          <stop offset="1" stop-color="var(--emerald-dark)"/>
        </linearGradient>
      </defs>
      <polygon points="80,0 112,0 398,40 398,150 300,372 268,372 2,210 0,170" fill="url(#emerald-large)"/>
    </svg>
    <h1 class="front__name">Dale Montrose</h1>
    <p class="front__phone">469 552 0187</p>
    <p class="front__address">P.O.Box 318827 Dallas,Tx.75219</p>
    <p class="front__field front__field--gem">Gem ID...........................................</p>
    <p class="front__field front__field--origin">Country of origin............................</p>
    <ul class="contacts">
      <li>
        <svg viewBox="0 0 22 22" aria-hidden="true"><rect x="1" y="4" width="20" height="14" fill="var(--gold)"/><polyline points="1,4 11,12 21,4" fill="none" stroke="var(--ruby-deep)" stroke-width="1.5"/></svg>
        belmo@postwire.example
      </li>
      <li>
        <svg viewBox="0 0 22 22" aria-hidden="true"><rect x="2" y="4" width="18" height="12" fill="none" stroke="var(--gold)" stroke-width="2.2"/><rect x="7" y="18" width="8" height="2" fill="var(--gold)"/></svg>
        www.bellavoregold.example
      </li>
      <li>
        <svg viewBox="0 0 22 22" aria-hidden="true"><circle cx="11" cy="11" r="10" fill="var(--gold)"/></svg>
        www.socialpage.example/BellavoreGold
      </li>
    </ul>
  </section>

  <section class="card card--back">
    <svg class="back__emerald" viewBox="0 0 97 97" role="img" aria-label="Photograph of an emerald-cut emerald">
      <defs>
        <linearGradient id="emerald-small" x1="0" y1="0" x2="1" y2="1">
          <stop offset="0" stop-color="var(--emerald-light)"/>
          <stop offset="0.5" stop-color="var(--emerald)"/>
          <stop offset="1" stop-color="var(--emerald-dark)"/>
        </linearGradient>
      </defs>
      <polygon points="12,0 85,0 97,12 97,85 85,97 12,97 0,85 0,12" fill="url(#emerald-small)"/>
    </svg>
    <h2 class="back__company">Bellavore/Gems</h2>
    <p class="back__est">Est.1972</p>
    <p class="back__certs">Importers of Colombian Emeralds<br>Emeralds over 1.0ct. certified for Gem ID and Country of origin – KSL,PRV</p>
    <p class="back__web">www.socialpage.example/BellavoreGold</p>
  </section>

</main>
</body>
</html>
```